Need a clean & modern homepage for an education site + opportunity for longer term work

Thanks for viewing our project. We are excited about this new website and we hope that we might build a relationship with designers as we work on this project. I provided quite a few details and requirements to help you more quickly create a design that meets our needs.
Who we are:
We are a website that discusses the importance of college accreditation and provides a directory of college programs.
What we need:
A homepage that meets the below requirements and is inspired by the examples provided
Definition of accredited:
ac·cred·it·ed [uh-kred-i-tid] adj.
1. officially recognized as meeting the essential requirements, as of academic excellence: accredited schools.
2. provided with official credentials, as by a government: an accredited diplomatic representative.
3. accepted as authoritative: an accredited theory.
Overall look and feel for the homepage:
- Clean, simple and modern
- Limited (or zero) pictures
- Utilize color blocks with text
- A trend seems to be longer vertical length homepages with lots of whitespace. I generally like this trend as long as the page is not way to tall.
Inspirations: Sites that have a similar look and feel to what I need.
http://plinvar.org/
http://www.tumbrelstat.com/colleges/harrowgate-university/
http://quietmarble.org/
http://www.vellichorstaffing.com/
http://www.plonk.com/
http://sketches.zimvo.com/
Items to be included on the homepage. Details below on each item.
- Top navigation
- Logo: Please leave a blank area for a logo. The logo has not been designed.
- Simple graphic/color block at the top that highlights a definition of “Accredited” – the definition should be formatted like it is being copy/pasted from a dictionary.
- Space for a video and small (50 word) written description of the video. You can use placeholder text.
- One section with 3 Paragraphs of content (each paragraph around 100 words) with a header at the top. You can use placeholder text but please create the formatting. At the end of the 3 paragraphs please have a “Read More” Note this shouldn't be 3 separate paragraphs with three read mores - it is 3 paragraphs with one read more at the end.
- An area with the header “Search Colleges by State” that has anchor text links to all 50 states.
Top navigation:
- Home
- States – with a subnav dropdown that includes all 50 US states.
- Programs – with a subnav dropdown that includes program titles (list below)
- Degrees - with a subnav dropdown that includes 5 degree levels (list below)
- Accreditation – no subnav
- Rankings – no subnav
- Resources – no subnav
Footer
- Link to about us, privacy, and a copyright www.url.com
Programs List for sub navigation
Accounting
Art
Bible
Business
Criminal Justice
Design
Engineering
English
Law
LPN to RN
Management
Math
MBA
MPH
Medical Assisting
Military
Nursing
Occupational Therapy
Paralegal
Psychology
Pharmacy
RN to BSN
Radiology
Social Work
Sonography
Degrees list for sub navigation
Certificate
Associate
Bachelors
Masters
PhD
Thanks so much - looking forward to working with you!

```html
<!DOCTYPE html>
<html lang="en">
<head>
<meta charset="utf-8">
<title>Education — Accredited</title>
<link href="https://fonts.googleapis.com/css2?family=Montserrat:wght@300;400;500&family=Roboto:wght@300;400&display=swap" rel="stylesheet">
<style>
:root{
  --nav-bg:#222222;
  --nav-text:#9a9a9a;
  --nav-active:#ffffff;
  --header-bg:#efefef;
  --rule:#dcdcdc;
  --logo-slot:#e2e2e2;
  --brand-red:#c1272d;
  --sky:#48bbdf;
  --sky-text:#45b9de;
  --body-gray:#8a8a8a;
  --copy-gray:#7a7a7a;
  --white:#ffffff;
}
*{margin:0;padding:0;box-sizing:border-box}
html,body{width:1200px;height:902px;overflow:hidden;background:var(--white)}
body{font-family:'Montserrat',sans-serif}
.wrap{width:800px;margin:0 auto;position:relative}
a{text-decoration:none;color:inherit}

.top-nav{height:32px;background:var(--nav-bg)}
.top-nav ul{list-style:none;display:flex;justify-content:space-between;height:32px;align-items:center}
.top-nav li{font-size:12.8px;color:var(--nav-text);letter-spacing:.4px}
.top-nav li.active{color:var(--nav-active)}
.top-nav .caret{font-size:10px;margin-left:3px}

.site-header{height:62px;background:var(--header-bg);border-bottom:1px solid var(--rule)}
.site-header .wrap{display:flex;justify-content:space-between;align-items:center;height:61px}
.logo-slot{width:181px;height:26px;background:var(--logo-slot)}
.state-link{font-size:12.8px;font-weight:500;color:var(--sky-text);letter-spacing:.6px}

.definition{background:var(--sky);height:220px;color:var(--white)}
.definition .wrap{padding-top:32px}
.term-row{display:flex;align-items:center}
.term{border:2px solid var(--white);width:150px;height:32px;font-size:20px;font-weight:500;text-align:center;line-height:29px}
.pron{font-size:10.5px;margin-left:10px;letter-spacing:.2px}
.senses{margin-top:30px;list-style:none;counter-reset:s}
.senses li{counter-increment:s;position:relative;padding-left:18px;font-size:14.4px;line-height:16.8px;margin-bottom:7px;letter-spacing:.1px}
.senses li::before{content:counter(s)".";position:absolute;left:0;top:1px}

.feature{height:219px}
.feature .wrap{display:flex;padding-top:32px}
.player{width:255px;height:155px;background:#0b0b0b;border:1px solid #333;position:relative;flex:none}
.player svg{display:block}
.feature-text{margin-left:19px}
.section-title{font-size:16px;font-weight:500;color:var(--brand-red);letter-spacing:.2px}
.feature-text p{margin-top:13px;margin-left:1px;font-size:11.8px;font-weight:300;line-height:17.6px;color:var(--body-gray);text-transform:uppercase;white-space:nowrap;letter-spacing:.1px}

.article{height:339px;background:linear-gradient(#efefef,#ffffff)}
.article .wrap{padding-top:31px}
.article .section-title{margin-left:-1px}
.article p{font-family:'Roboto',sans-serif;font-weight:300;font-size:9.9px;line-height:14.4px;color:var(--copy-gray);white-space:nowrap}
.article .section-title + p{margin-top:10px}
.article p + p{margin-top:14.4px}
.read-more{display:inline-block;margin-top:22px;background:var(--brand-red);color:var(--white);font-size:10.5px;font-weight:500;width:70px;height:27px;line-height:27px;text-align:center}

.site-footer{height:30px;background:var(--nav-bg);text-align:center;font-family:'Roboto',sans-serif;font-size:9.6px;line-height:30px;color:var(--copy-gray)}
.site-footer .sep{margin:0 5px}
</style>
</head>
<body>
<nav class="top-nav">
  <ul class="wrap">
    <li class="active">HOME</li>
    <li>STATES<span class="caret">▼</span></li>
    <li>PROGRAMS<span class="caret">▼</span></li>
    <li>DEGREES<span class="caret">▼</span></li>
    <li>ACCREDITATION</li>
    <li>RANKINGS</li>
    <li>RESOURCES</li>
  </ul>
</nav>

<header class="site-header">
  <div class="wrap">
    <div class="logo-slot" role="img" aria-label="Logo placeholder"></div>
    <a class="state-link" href="#">SEARCH COLLEGES BY STATE</a>
  </div>
</header>

<section class="definition">
  <div class="wrap">
    <div class="term-row">
      <div class="term">ACCREDITED</div>
      <div class="pron">AC·CRED·IT·ED &nbsp;[UH-KRED-I-TID] ADJ.</div>
    </div>
    <ol class="senses">
      <li>OFFICIALLY RECOGNIZED AS MEETING THE ESSENTIAL REQUIREMENTS, AS OF ACADEMIC EXCELLENCE: ACCREDITED SCHOOLS.</li>
      <li>PROVIDED WITH OFFICIAL CREDENTIALS, AS BY A GOVERNMENT: AN ACCREDITED DIPLOMATIC REPRESENTATIVE.</li>
      <li>ACCEPTED AS AUTHORITATIVE: AN ACCREDITED THEORY.</li>
    </ol>
  </div>
</section>

<section class="feature">
  <div class="wrap">
    <div class="player">
      <svg width="253" height="153" viewBox="0 0 253 153">
        <circle cx="127" cy="72" r="27" fill="#2a2a2a" stroke="#3a3a3a"/>
        <path d="M119 60 L139 72 L119 84 Z" fill="#bfbfbf"/>
        <rect x="0" y="133" width="253" height="20" fill="#1c1c1c"/>
        <path d="M7 139 L12 143 L7 147 Z" fill="#ddd"/>
        <rect x="16" y="142" width="124" height="3" fill="#444"/>
        <rect x="16" y="142" width="50" height="3" fill="#c1272d"/>
        <rect x="66" y="142" width="30" height="3" fill="#777"/>
        <text x="143" y="146" font-family="Roboto,sans-serif" font-size="7" fill="#ddd">1:26 / <tspan fill="#888">3:22</tspan></text>
        <path d="M181 140 h2 l3 -2 v9 l-3 -2 h-2 Z" fill="#ddd"/>
        <rect x="190" y="142" width="24" height="3" fill="#444"/>
        <rect x="190" y="142" width="15" height="3" fill="#c1272d"/>
        <line x1="219" y1="134" x2="219" y2="153" stroke="#333"/>
        <rect x="224" y="140" width="8" height="6" fill="none" stroke="#ddd"/>
        <text x="237" y="146" font-family="Roboto,sans-serif" font-size="7" font-weight="700" font-style="italic" fill="#ddd">HD</text>
      </svg>
    </div>
    <div class="feature-text">
      <h2 class="section-title">Lorem Ipsum Dolor sot amet</h2>
      <p>Lorem ipsum dolor sit amet, consectetur adipiscing elit. Nunc porta<br>tempus ullamcorper. Vivamus porta mauris vel mollis lobortis.<br>Suspendisse massa justo, auctor et lectus eu, cursus pulvinar nunc.<br>Nam sodales venenatis justo et eleifend. Morbi nec auctor dolor,<br>ac rutrum erat. Nullam tincidunt est ut augue pulvinar imperdiet.<br>Vivamus at.</p>
    </div>
  </div>
</section>

<section class="article">
  <div class="wrap">
    <h2 class="section-title">Lorem Ipsum Dolor sot amet</h2>
    <p>Lorem ipsum dolor sit amet, consectetur adipiscing elit. Fusce in dignissim nisi. Proin elementum justo in ante fermentum sodales. Aliquam convallis mi at placerat posuere. In hac<br>habitasse platea dictumst. Curabitur vel risus aliquet, eleifend arcu sit amet, ornare massa. Duis odio felis, pulvinar et eros nec, scelerisque gravida risus. Nulla sed dignissim nisi.<br>Morbi laoreet dolor eu tristique fringilla. Nulla blandit blandit dui, ac malesuada augue ultrices tempor. Aliquam erat volutpat. Nam vestibulum in sapien eget dignissim. Duis tincidunt,<br>magna non convallis iaculis, elit risus ultricies ipsum, eget ullamcorper tortor turpis tempus arcu. Pellentesque commodo, lorem a bibendum dapibus.</p>
    <p>Pellentesque habitant morbi tristique senectus et netus et malesuada fames ac turpis egestas. Etiam gravida tristique urna. Aenean faucibus ipsum tortor, at aliquet est feugiat a.<br>Proin egestas vitae augue vel molestie. Phasellus quis tellus est. Aenean convallis rhoncus egestas. Cras aliquet interdum vehicula. Suspendisse id sem eget neque pellentesque<br>gravida vel ut nisl. Praesent diam neque, faucibus vitae hendrerit vitae, commodo ac risus. Etiam eleifend sit amet magna sed tincidunt. Quisque dictum ultricies nisl. Suspendisse<br>rutrum lectus in est malesuada, eu pretium nisi tristique. Nulla facilisi. Fusce vehicula sed lectus id elementum. Nunc faucibus, eros in rutrum ornare, nibh.</p>
    <p>Fusce sodales scelerisque ipsum, id imperdiet urna pretium a. Donec augue tortor, placerat vel nunc eu, euismod vehicula neque. Phasellus convallis nisi eget velit pulvinar commodo.<br>Pellentesque ultricies quis ante sit amet tincidunt. Vivamus sodales risus lorem, vel posuere mi posuere pellentesque. Fusce nibh metus, rhoncus et venenatis eu, convallis ut odio.<br>Curabitur auctor lorem id metus blandit, ac euismod dui suscipit. Quisque ac posuere turpis. Etiam risus tellus, iaculis et est a, varius tempor diam. Duis in nibh nibh. Etiam iaculis nec<br>mauris sed aliquam. Nulla facilisi. Aliquam consequat justo sed tortor aliquam, at aliquam massa bibendum. Donec viverra</p>
    <a class="read-more" href="#">Read More</a>
  </div>
</section>

<footer class="site-footer">
  Copyright © 2013<span class="sep">|</span>About Us<span class="sep">|</span>Privacy Policy<span class="sep">|</span>www.url.com
</footer>
</body>
</html>
```